Design a Flyer for new Irish Dancing school

We need an A5 flyer designer for new Irish Dancing school. See details in attached file. We need the finished designs delivered in Photoshop and PDF formats.

```html
<!DOCTYPE html>
<html lang="en">
<head>
<meta charset="utf-8">
<title>Whelan Academy of Irish Dancing – Flyer</title>
<link href="https://fonts.googleapis.com/css2?family=Pirata+One&family=Playfair+Display+SC:wght@700&family=Roboto+Condensed:wght@700&display=swap" rel="stylesheet">
<style>
  :root {
    --orange: #f57c0f;
    --green: #0f8b3d;
    --green-dark: #0a7a33;
    --white: #ffffff;
    --photo-light: #e98a55;
    --photo-mid: #c9643a;
    --photo-dark: #4a1d0c;
    --engrave: #c9c9c9;
  }
  * { margin: 0; padding: 0; box-sizing: border-box; }
  html, body { width: 846px; height: 1200px; overflow: hidden; background: var(--orange); }
  .flyer {
    position: relative;
    width: 846px;
    height: 1200px;
    overflow: hidden;
    color: var(--white);
    font-family: "Roboto Condensed", "Arial Narrow", sans-serif;
    font-weight: 700;
    text-transform: uppercase;
  }
  .band { position: absolute; left: 0; width: 100%; }
  .masthead { top: 0; height: 371px; background: var(--orange); text-align: center; }
  .academy {
    position: absolute; top: 30px; left: 0; width: 100%;
    font-family: "Pirata One", serif;
    font-weight: 400;
    text-transform: none;
    font-size: 42px;
    letter-spacing: 1px;
  }
  .title {
    position: absolute; left: 0; width: 100%;
    font-family: "Playfair Display SC", serif;
    font-weight: 700;
    line-height: 1;
    text-shadow: 3px 3px 0 var(--engrave);
  }
  .title-irish { top: 92px; font-size: 132px; letter-spacing: 6px; }
  .title-dancing { top: 214px; font-size: 132px; letter-spacing: 3px; }

  .start { top: 371px; height: 124px; background: var(--green); display: flex; align-items: center; justify-content: center; font-size: 50px; letter-spacing: 0.5px; }

  .schedule { top: 495px; height: 127px; background: var(--orange); text-align: center; }
  .schedule-time { position: absolute; top: 14px; width: 100%; font-size: 44px; }
  .schedule-venue { position: absolute; top: 68px; width: 100%; font-size: 35px; }

  .divider { top: 622px; height: 18px; background: var(--green); }

  .photo {
    top: 640px; height: 368px;
    background: linear-gradient(180deg, var(--photo-light) 0%, var(--photo-mid) 60%, var(--photo-dark) 100%);
  }
  .photo-caption {
    position: absolute; top: 272px; left: 0; width: 100%;
    display: flex; justify-content: center; gap: 48px;
    font-size: 36px;
  }

  .labels { top: 1008px; height: 59px; background: var(--orange); font-size: 34px; }
  .details { top: 1067px; height: 133px; background: var(--green); font-size: 38px; line-height: 48px; }
  .col-left { position: absolute; left: 33px; }
  .col-right { position: absolute; left: 588px; }
  .labels .col-left, .labels .col-right { top: 8px; }
  .details .col-left, .details .col-right { top: 16px; }
</style>
</head>
<body>
<main class="flyer">
  <header class="band masthead">
    <p class="academy">Whelan Academy of</p>
    <h1>
      <span class="title title-irish">IRISH</span>
      <span class="title title-dancing">DANCING</span>
    </h1>
  </header>

  <section class="band start">Commencing September 2013</section>

  <section class="band schedule">
    <p class="schedule-time">Thursdays 3pm to 4pm</p>
    <p class="schedule-venue">Kilbarrow Sports and Leisure Centre (KSLC)</p>
  </section>

  <div class="band divider"></div>

  <section class="band photo" role="img" aria-label="Photo of Irish dancers' legs in white socks and laced dance shoes, mid-leap">
    <p class="photo-caption"><span>Age: 4+ years</span><span>Beginners welcome!</span></p>
  </section>

  <section class="band labels">
    <p class="col-left">Teachers:</p>
    <p class="col-right">Contact:</p>
  </section>

  <section class="band details">
    <p class="col-left">Aoife Whelan T.C.R.G<br>Niamh Whelan T.C.R.G</p>
    <p class="col-right">086-0412378<br>087-5590132</p>
  </section>
</main>
</body>
</html>
```